Soccer Club Site Redesign

We are a suburban youth soccer club in need of a web site redesign. Our current site’s look/feel is outdated and is in need of a more modern look. What we are looking for is a design layout that will accommodate the current functionality we have for the site and give us an updated modern look. The deliverable for this project will be .psd file that can be converted to an html theme file for Wordpress. We will take care of the conversion and handle the html coding/javascript functionality.
Take a look at our current site to get an idea of what we offer and the current layout we have.
http://www.torvelkicks.org
Our club hosts youth recreational soccer, traveling soccer and two large soccer tournaments during the year. We also sponsor a number of training clinics. Our site serves a couple primary purposes:
1. Parents learn how/where/when to sign up their child for the leagues we offer.
2. Parents learn dates/times of various events the club offers.
3. Other soccer clubs get information on the tournaments we offer, sign up for the tournaments etc.
We do a pretty good job of presenting information about the various events/leagues available and how to sign up for them, but we want to do a better job of presenting a calendar where parents can quickly find dates/times of various events. Ideally, we would like to incorporate a news section (like we currently have), with a calendar and the use of more images on the home page. We understand screen space is limited but would incorporate jquery/javascript widgets to hide/show info and maybe an ‘imagebox’ for the additional images.
Here are a few sites with ideas that we liked:
http://sports.brenwickcollege.edu/ (Look at the Upcoming Events calendar on the page)
http://www.fennlowfutbol.com/ (look at the Upcoming Events calendar in the right column and the image box in the main content area)
http://www.rundlekick.com/index.php (Like the look and use of images)
http://www.qvfootyclub.com/ (imagebox use)
http://www.sarvapuckclub.org/ ( hockey website but like the use of crisp header graphics)
http://www.delvingpuckers.com/ (another hockey site, like the calendar used)
That should give you a pretty good idea of what we are looking for. The new design will need to accommodate the existing functionality of the site. Our logo (which is attached) should be incorporated into the site….otherwise we are open to your design ideas.

```html
<!DOCTYPE html>
<html lang="en">
<head>
<meta charset="utf-8">
<title>Torvel Soccer Club</title>
<link href="https://fonts.googleapis.com/css2?family=Open+Sans:wght@400;600;700&family=Arimo:wght@400;700&family=Russo+One&display=swap" rel="stylesheet">
<style>
:root{
  --bg-dark:#1b1a18;
  --band:#2b2b2b;
  --panel:#111;
  --card:#252525;
  --item:#121212;
  --red:#c8161b;
  --red-dark:#9b0f12;
  --blue:#1b2ec4;
  --blue-deep:#0a1266;
  --text:#fff;
  --muted:#b9b9b9;
}
*{box-sizing:border-box;margin:0;padding:0}
html,body{width:1050px;height:1200px;overflow:hidden}
body{position:relative;font-family:"Open Sans",sans-serif;color:var(--text);background:var(--bg-dark)}
.page-backdrop{position:absolute;inset:0;background:
  radial-gradient(ellipse at 50% 0%,#e8e4dc 0%,#b8aa98 18%,transparent 40%),
  radial-gradient(ellipse at 20% 60%,#6d5a48 0%,transparent 45%),
  radial-gradient(ellipse at 85% 55%,#7a6652 0%,transparent 45%),
  linear-gradient(180deg,#cfc8bc 0%,#8a7462 35%,#4b4a3a 70%,#27351e 100%)}
.btn{position:absolute;background:var(--red);color:#fff;font-size:12px;text-align:center;text-transform:uppercase;border-radius:1px}
.top-btn{top:16px;height:23px;line-height:23px}
.header-band{position:absolute;left:0;top:58px;width:1050px;height:92px;background:rgba(38,38,38,.95)}
.club-mark{position:absolute;left:108px;top:82px;display:flex;align-items:center;gap:8px;font-family:"Russo One",sans-serif;font-size:20px;color:#fff}
.club-mark .dot{width:26px;height:26px;border-radius:50%;background:var(--blue)}
.welcome{position:absolute;left:256px;top:80px;font-family:"Russo One",sans-serif;white-space:nowrap}
.welcome small{font-size:28px}
.welcome strong{font-size:38px;font-weight:400}
.main-nav{position:absolute;left:106px;top:196px;width:146px;height:392px;background:var(--blue-deep);list-style:none}
.main-nav li{height:28px;line-height:28px;text-align:center;font-size:11px;font-weight:600;border-bottom:1px solid #3446c9;background:linear-gradient(180deg,#0b136c,#1e34c8 55%,#0d188a)}
.slider{position:absolute;left:270px;top:196px;width:675px;height:392px;border:4px solid #2a2a2a;background:linear-gradient(180deg,#d7d6d2 0%,#bbb9b2 30%,#567a3a 55%,#3d5f2a 100%)}
.slide-caption{position:absolute;left:0;right:0;bottom:0;height:78px;background:rgba(15,15,15,.78)}
.slide-caption h2{position:absolute;left:88px;top:20px;font-size:15px;font-weight:600}
.slide-caption p{position:absolute;left:88px;top:46px;font-family:Arimo,sans-serif;font-size:10px;color:#ddd;white-space:nowrap}
.arrow{position:absolute;top:24px}
.content-panel{position:absolute;left:105px;top:628px;width:840px;height:372px;background:var(--panel);border-radius:6px}
.col{position:absolute;top:16px;height:341px;background:var(--card);border-radius:3px}
.col h3{position:absolute;left:13px;top:12px;font-size:21px;font-weight:400}
.news-item{position:absolute;left:9px;width:245px;height:46px;background:var(--item);border-radius:3px;padding:8px 9px;font-family:Arimo,sans-serif;white-space:nowrap;overflow:hidden}
.news-item b{display:block;font-weight:400;font-size:11px;line-height:14px}
.news-item span{display:block;font-size:9.5px;line-height:12px;color:var(--muted);margin-top:3px}
.event-photo{position:absolute;left:16px;top:46px;width:235px;height:125px;border:2px solid #a2161a;background:linear-gradient(180deg,#dfe8f2 0%,#9fb2c2 35%,#4d7a35 60%,#3c6428 100%)}
.event-text{position:absolute;left:16px;top:178px;width:240px;font-family:Arimo,sans-serif;font-size:10px;line-height:1.35;color:#ddd}
.event-text strong{display:block;color:#fff;font-size:10.5px;line-height:1.55;margin-bottom:6px}
.event-text p{margin-bottom:8px}
.cal{position:absolute;left:15px;width:230px;height:60px}
.cal .month{position:absolute;left:0;top:0;font-family:Arimo,sans-serif;font-size:8px}
.cal .day{position:absolute;left:6px;top:11px;font-size:33px;font-weight:700;line-height:1}
.cal .desc{position:absolute;left:76px;top:4px;width:165px;font-family:Arimo,sans-serif;font-size:11px;line-height:1.35}
.read-more{top:987px;height:23px;line-height:23px;width:87px}
.travel-banner{position:absolute;left:106px;top:1041px;width:607px;height:86px;background:linear-gradient(90deg,#1b4fc6 0%,#2057d8 40%,#3a1f6e 70%,#2a55c8 100%)}
.ball{position:absolute;left:2px;top:3px;width:80px;height:80px;border-radius:50%;background:radial-gradient(circle at 40% 35%,#fff,#bdbdbd)}
.travel-banner h4{position:absolute;left:104px;top:24px;font-size:29px;font-weight:600}
.register{position:absolute;left:431px;top:20px;width:178px;height:46px;line-height:46px;border-radius:8px;background:linear-gradient(180deg,#e0242a,var(--red-dark));font-size:17px;font-weight:700;text-align:center}
.partners{position:absolute;left:733px;top:1041px;width:213px;height:87px;background:#fff;border-radius:3px;display:flex;align-items:center;justify-content:space-around;color:#1a1a1a;font-weight:700;font-size:13px}
.copyright{position:absolute;left:0;width:1050px;top:1163px;text-align:center;font-size:10px}
</style>
</head>
<body>
<div class="page-backdrop" role="img" aria-label="Blurred photo of youth soccer players on a field"></div>

<a class="btn top-btn" style="left:801px;width:64px">Log In</a>
<a class="btn top-btn" style="left:879px;width:66px">Sign Up</a>

<header class="header-band"></header>
<div class="club-mark"><span class="dot"></span>TORVEL</div>
<h1 class="welcome"><small>WELCOME TO THE </small><strong>TORVEL SOCCER CLUB!</strong></h1>

<ul class="main-nav">
  <li>HOME</li><li>ABOUT US</li><li>FORMS</li><li>CALENDAR</li><li>TRAVELING</li><li>RECREATIONAL</li><li>TOURNAMENTS</li><li>REFEREES</li><li>FIELD MAPS</li><li>TEAM MANAGERS</li><li>VOLUNTEERS</li><li>CONTACT US</li><li>SPONSORS</li><li>LINKS</li>
</ul>

<section class="slider" role="img" aria-label="Photo of young players practicing ball drills with a coach">
  <div class="slide-caption">
    <svg class="arrow" style="left:21px" width="32" height="32" viewBox="0 0 32 32"><circle cx="16" cy="16" r="16" fill="#fff"/><path d="M19 9l-7 7 7 7" stroke="#111" stroke-width="3.5" fill="none"/></svg>
    <h2>LOREM IPSUM SIT AMET</h2>
    <p>Lorem ipsum dolor sit amet, consectetur adipiscing elit. Donec euismod sodales est, eget semper magna.</p>
    <svg class="arrow" style="left:614px" width="32" height="32" viewBox="0 0 32 32"><circle cx="16" cy="16" r="16" fill="#fff"/><path d="M13 9l7 7-7 7" stroke="#111" stroke-width="3.5" fill="none"/></svg>
  </div>
</section>

<main class="content-panel">
  <section class="col" style="left:15px;width:263px">
    <h3>LATEST NEWS</h3>
    <div class="news-item" style="top:47px"><b>Integer mauris. Cras iaculis viverra dolorqw.</b><span>Nulla suscipit. Proin eu sapien ac sem</span></div>
    <div class="news-item" style="top:107px"><b>Integer mauris. Cras iaculis viverra dolorqw.</b><span>Nulla suscipit. Proin eu sapien ac sem</span></div>
    <div class="news-item" style="top:166px"><b>Integer mauris. Cras iaculis viverra dolorqw.</b><span>Nulla suscipit. Proin eu sapien ac sem</span></div>
    <div class="news-item" style="top:226px"><b>Integer mauris. Cras iaculis viverra dolorqw.</b><span>Nulla suscipit. Proin eu sapien ac sem</span></div>
    <div class="news-item" style="top:286px"><b>Integer mauris. Cras iaculis viverra dolorqw.</b><span>Nulla suscipit. Proin eu sapien ac sem</span></div>
  </section>
  <section class="col" style="left:293px;width:263px">
    <h3>TOP EVENTS</h3>
    <div class="event-photo" role="img" aria-label="Photo of children running after the ball in a game"></div>
    <div class="event-text">
      <strong>Lorem ipsum dolor sit amet, consectetur adipi-scing elit.</strong>
      <p>Integer mi sem, volutpat in ultricies nec, venenatis nec nisl. Morbi non tellus a dui ornare sagittis.</p>
      <p>Praesent at nibh ac dolor adipiscing aliquam vitae ornare eros.</p>
      <p>Duis ornare sagittis ipsum in interdum. Proin justo justo, consequat at vulputate et, suscipit a.</p>
    </div>
  </section>
  <section class="col" style="left:570px;width:257px">
    <h3>UPCOMING EVENTS</h3>
    <div class="cal" style="top:62px"><span class="month">NOVEMBER</span><span class="day">02</span><div class="desc">Delta North Executive Commit-tee Election applications due - ( 1 pm - 4 pm )</div></div>
    <div class="cal" style="top:133px"><span class="month">NOVEMBER</span><span class="day">05</span><div class="desc">Tournament Weekend - ( 12 pm - 5 pm )<br>(05/09/2012 - 06/09/2012)</div></div>
    <div class="cal" style="top:204px"><span class="month">NOVEMBER</span><span class="day">09</span><div class="desc">Tournament Weekend - ( 1 pm - 4 pm )<br>(09/09/2012 - 10/09/2012)</div></div>
    <div class="cal" style="top:275px"><span class="month">NOVEMBER</span><span class="day">12</span><div class="desc">District Commissioner Meeting<br>- ( 11 am - 12 pm )</div></div>
  </section>
</main>

<a class="btn read-more" style="left:130px">Read More</a>
<a class="btn read-more" style="left:412px">Read More</a>
<a class="btn read-more" style="left:690px">Read More</a>

<section class="travel-banner">
  <div class="ball" role="img" aria-label="Soccer ball illustration"></div>
  <h4>2013 TRAVEL SOCCER</h4>
  <a class="register">REGISTER HERE</a>
</section>

<aside class="partners">
  <span>Northland Youth Soccer</span>
  <span>Strivo</span>
</aside>

<footer class="copyright">COPYRIGHT © TORVEL SOCCER CLUB 2012</footer>
</body>
</html>
```